Executive Summary

Create a one page executive summary of a venture fund - with the information here:
https://files.brindlecove.net/d/7qTm3VxR9pLw2KcYhN8sD4fBzJ6gA1eUoXiM5tQrWnE/view?share=open

```html
<!DOCTYPE html>
<html lang="en">
<head>
<meta charset="utf-8">
<title>Meridian Decarbonization Partnership Fund — Executive Summary</title>
<link rel="stylesheet" href="https://fonts.googleapis.com/css2?family=Nunito+Sans:wght@400;700;800&display=swap">
<style>
  :root {
    --bg: #9a9a9a;
    --paper: #ffffff;
    --ink: #1c1c1c;
    --muted: #555555;
    --blue: #1f6fbf;
    --magenta: #a21f5e;
    --orange: #f26a2b;
    --cyan: #1ba7e1;
    --purple: #8b2d8e;
    --teal: #17a49f;
    --red: #ea4236;
    --line: #333333;
  }
  * { box-sizing: border-box; margin: 0; padding: 0; }
  html, body { width: 1200px; height: 1200px; overflow: hidden; }
  body { background: var(--bg); font-family: "Nunito Sans", Arial, sans-serif; color: var(--ink); }
  .sheet {
    position: absolute; left: 475px; top: 10px; width: 250px; height: 1180px;
    background: var(--paper); overflow: hidden;
  }
  .tiny { font-size: 3.6px; line-height: 1.45; }
  .center { text-align: center; }
  .masthead { height: 114px; padding-top: 30px; text-align: center; }
  .masthead h1 { color: var(--blue); font-size: 12.5px; font-weight: 800; line-height: 1.25; }
  .masthead .subtitle { font-size: 6.2px; margin-top: 22px; }
  .masthead .byline { font-size: 3.8px; margin-top: 5px; color: var(--muted); }
  .thesis { margin: 8px 12px 0; height: 80px; background: var(--magenta); color: #fff; padding: 5px 10px; }
  .thesis h2 { font-size: 11px; font-weight: 800; text-align: center; }
  .thesis p { font-size: 3.4px; line-height: 1.4; margin-top: 2px; }
  .thesis p b { font-weight: 700; }
  .section-title { font-size: 10.5px; font-weight: 800; text-align: center; }
  .focus { margin-top: 13px; height: 52px; padding: 0 22px; }
  .focus p { margin-top: 4px; text-align: center; }
  .tag { display: block; width: 64px; margin: 0 auto; color: #fff; font-size: 8.5px; font-weight: 800; text-align: center; height: 16px; line-height: 16px; }
  .tag.orange { background: var(--orange); }
  .tag.cyan { background: var(--cyan); width: 128px; }
  .team { position: relative; height: 146px; margin: 6px 12px 0; }
  .member { position: absolute; width: 150px; text-align: center; }
  .member .name { font-size: 3.8px; font-weight: 700; }
  .member .bio { font-size: 3.2px; line-height: 1.4; color: var(--muted); }
  .portrait-slot { position: absolute; width: 22px; height: 22px; border: 0.8px solid var(--line); background: #fff; }
  .strategic { height: 150px; padding: 0 12px; }
  .strategic .section-title { margin-bottom: 8px; }
  .benefit-grid { display: grid; grid-template-columns: 1fr 1fr; gap: 5px; }
  .benefit { height: 60px; border-radius: 4px; color: #fff; padding: 4px 5px; }
  .benefit.purple { background: var(--purple); }
  .benefit.cyan { background: var(--cyan); }
  .benefit h3 { font-size: 3.8px; font-weight: 800; margin-bottom: 3px; }
  .benefit p { font-size: 3.2px; line-height: 1.4; }
  .terms { height: 84px; padding: 0 50px; margin-top: 2px; }
  .terms ul { list-style: none; margin-top: 5px; }
  .terms li { font-size: 3.3px; line-height: 1.45; }
  .record-table { margin: 7px 24px 0; width: 202px; border-collapse: collapse; font-size: 3.4px; }
  .record-table th { text-align: left; font-weight: 800; padding-bottom: 3px; vertical-align: top; }
  .record-table td { padding: 3.6px 0; }
  .fund-one { margin-top: 22px; }
  .fund-one h2 { font-size: 6.8px; font-weight: 800; text-align: center; }
  .fund-one ul { list-style: none; margin: 5px 0 0 70px; }
  .fund-one li { font-size: 3.3px; line-height: 1.45; }
  .portfolio { position: absolute; left: 0; top: 857px; width: 250px; height: 275px; background: var(--teal); color: #fff; padding: 8px 10px; }
  .portfolio h2 { font-size: 9px; font-weight: 800; text-align: center; margin-bottom: 5px; }
  .case { margin-bottom: 7px; }
  .case h3 { font-size: 3.6px; font-weight: 800; }
  .case p { font-size: 3.4px; line-height: 1.42; margin-bottom: 3px; }
  .case .quote-by { font-weight: 700; }
  .join { position: absolute; left: 0; top: 1132px; width: 250px; height: 48px; background: var(--red); color: #fff; text-align: center; padding-top: 6px; }
  .join h2 { font-size: 9px; font-weight: 800; }
  .join p { font-size: 3.2px; line-height: 1.4; }
</style>
</head>
<body>
<main class="sheet">
  <header class="masthead">
    <h1>Meridian Decarbonization<br>Partnership&nbsp; Fund</h1>
    <p class="subtitle">Designed for Corporate Decarbonization</p>
    <p class="byline">Partnerships, Presented by Meridian Capital</p>
  </header>

  <section class="thesis">
    <h2>Thesis</h2>
    <p class="center">Investing in Early-Stage Decarbonization Startups companies</p>
    <p><b>Collaboration:</b><br>Corporate LP network + collaborative Deals, Insights, Co-investment, and Exits</p>
    <p><b>Goals:</b><br>Acceleration of Decarbonization + Strategic and financial returns</p>
    <p><b>Impact:</b><br>Gt CO2e reduction potential per portfolio, reduced by 2030</p>
  </section>

  <section class="focus">
    <h2 class="section-title">Investment Focus</h2>
    <p class="tiny">We invest in Frontier Decarbonization Technologies that Accelerate Venture Returns and Strategic value for corporates LPs, such as:<br>AI &amp; Robotics • Energy Efficiency • Deep Decarbonization • Clean Energy • Advanced Synthetic Biology • Circular Materials • Sustainable Food • Electrification • Carbon Management</p>
  </section>

  <span class="tag orange">Team</span>
  <section class="team">
    <div class="portrait-slot" style="left:0;top:4px"></div>
    <div class="member" style="left:38px;top:4px"><p class="name">Iris Lorne, Co-Managing Partner (California)</p><p class="bio">Climate investor over a decade, PhD in clean energy and former founder and venture investor, MBA</p></div>
    <div class="portrait-slot" style="right:0;top:18px"></div>
    <div class="member" style="left:30px;top:20px"><p class="name">Malee Tanawong, PhD, Venture Partner (Thailand)</p><p class="bio">Faculty in Chemical Engineering at a national university in Bangkok, supporter of low-carbon engineering, PhD, former Engineering Co-founder of a deep tech startup</p></div>
    <div class="portrait-slot" style="left:0;top:42px"></div>
    <div class="member" style="left:38px;top:44px"><p class="name">Jalen Hoyle, PhD, Venture Partner (New York)</p><p class="bio">Serial deep tech entrepreneur, industry expertise in photonics and semiconductors, PhD in Applied Physics</p></div>
    <div class="portrait-slot" style="right:0;top:60px"></div>
    <div class="member" style="left:30px;top:64px"><p class="name">Cora Dune, CFA, Vice President (California)</p><p class="bio">Veteran investor in energy transition, 10+ years of experience in capital markets, energy, sustainability and innovation, MBA</p></div>
    <div class="portrait-slot" style="left:0;top:84px"></div>
    <div class="member" style="left:38px;top:86px"><p class="name">Tessa Kell, Chief of Staff (California)</p><p class="bio">Previous experience in VC and legal, MBA candidate</p></div>
    <div class="portrait-slot" style="right:0;top:104px"></div>
    <div class="member" style="left:30px;top:100px"><p class="name">Amber Sorrel, J.D., Legal Advisor (New York)</p><p class="bio">Senior Counsel at deep technology ventures, J.D., long tenure in venture law</p></div>
  </section>

  <section class="strategic">
    <h2 class="section-title">Design for Strategic Investors</h2>
    <div class="benefit-grid">
      <div class="benefit purple"><h3>Deal Flow Access</h3><p><b>Weekly Call Reviews</b><br>• LPs receive first look at top startups<br><b>Startup Pipeline</b><br>• Curated deal list matched to corporate goals</p></div>
      <div class="benefit cyan"><h3>Sector Intelligence</h3><p><b>Research Reports</b><br>• Trends on climate sectors, insights and data<br><b>Knowledge Exchange</b><br>• Workshops and roundtables<br><b>Sector Workshops</b><br>• Deep dives with founders</p></div>
      <div class="benefit cyan"><h3>Aligned Co-Investment</h3><p><b>Co-Investment Network</b><br>• Invest with other corporates in proven portfolio companies<br><b>Due Diligence Support</b><br>• Shared technical and commercial reviews</p></div>
      <div class="benefit purple"><h3>Tailored Engagement, Dependent on Investment Level</h3><p><b>Custom Deal Sourcing</b><br>• Pipeline by target area<br><b>Private Access Briefings</b><br>• Quarterly one-on-one sessions<br><b>Strategic GP Access</b><br>• Direct line to partners</p></div>
    </div>
  </section>

  <section class="terms">
    <h2 class="section-title">Fund Term Overview</h2>
    <ul>
      <li>• Fund Size: $50M</li>
      <li>• Term: 10+1+1 Years</li>
      <li>• Stage: Pre-seed, Series A (lead), Series A (follow)</li>
      <li>• Target Returns: 3x of Invested Capital, 25% IRR</li>
      <li>• Check Size: $1-3M, 30% kept for follow-ons</li>
      <li>• Portfolio: 25 to 30 companies</li>
      <li>• Geography: US, Asia, Europe</li>
      <li>• Fees: 2% management fee, carried interest 20% above hurdle</li>
      <li>• Close: 2026</li>
    </ul>
  </section>

  <span class="tag cyan">Track Record</span>
  <table class="record-table">
    <thead><tr><th>Company (Fund I Exit/ Priced Round)</th><th>Stage Invested</th><th>Current stage</th></tr></thead>
    <tbody>
      <tr><td>Clearwell</td><td>Series A Bridge 2022</td><td>Series C 4.4B</td></tr>
      <tr><td>Basalto</td><td>Seed 2019</td><td>Growth Stage $250M</td></tr>
      <tr><td>Helion Diamonds</td><td>Seed 2021</td><td>Series A 47.4M</td></tr>
      <tr><td>Ferrum Infrastructure</td><td>Seed Extension 2021</td><td>Series B $80M</td></tr>
      <tr><td>Vireo Bio</td><td>Pre-Seed 2019</td><td>Series A 12.6M</td></tr>
    </tbody>
  </table>

  <section class="fund-one">
    <h2>Fund I Investments so far (continue to invest)</h2>
    <ul>
      <li>• Tessar Carbon ($1.5M Seed, leading Series A)</li>
      <li>• Northwind Materials (Seed)</li>
      <li>• Verdant Foods ($1.4M Seed)</li>
      <li>• Lumen Grid (Seed)</li>
      <li>• Ashfield (Pre-seed)</li>
      <li>• Halomaris (Seed)</li>
    </ul>
  </section>

  <section class="portfolio">
    <h2>Example Portfolio Startups</h2>
    <div class="case">
      <h3>Clearwell: modular green methanol production</h3>
      <p>Clearwell has built a compact electrochemical process that turns captured CO2 and renewable power into green methanol, cutting capital cost and plant footprint compared with legacy production. The modular units can be placed next to industrial emitters, ports and chemical sites, so customers avoid long supply chains and can decarbonize fuel and feedstock at the same time. Since our bridge investment the company has signed offtake agreements with shipping and chemical customers and has grown its team across engineering, manufacturing and sales.</p>
      <p>"Our early partners opened doors with strategic buyers and helped shape our first commercial deployments, long before others saw the market." <span class="quote-by">— Founder and CEO, Clearwell</span></p>
    </div>
    <div class="case">
      <h3>Helion Diamonds: lab-grown diamond semiconductors</h3>
      <p>Helion grows synthetic diamond wafers for power electronics that run cooler, switch faster and waste far less energy than silicon parts. The team scaled from a single pilot reactor to commercial supply in under three years, and now works with several corporate partners on data centre, electric vehicle and grid applications where heat and efficiency matter most.</p>
      <p>"The fund's network gave us technical reviews and the right introductions at a critical moment in our growth." <span class="quote-by">— CEO and Co-founder, Helion Diamonds</span></p>
    </div>
    <div class="case">
      <h3>Ferrum: low-carbon steel for infrastructure</h3>
      <p>Ferrum uses hydrogen-ready processes to produce structural steel with a fraction of the emissions of blast furnace routes. Strategic co-investors joined the round after shared diligence led by our partners, and the company now supplies pilot projects across three regions. Commercial contracts with builders and utilities are expected to grow through the next funding round, as buyers look for verified low-carbon materials to meet their own climate targets and reporting needs.</p>
      <p>"A partner who truly understands hard tech, long build cycles and patient capital, and who stays close to us at every step." <span class="quote-by">— CFO and Co-founder, Ferrum</span></p>
    </div>
  </section>

  <section class="join">
    <h2>Join Us</h2>
    <p>For any inquiries please contact<br>Iris Lorne<br>Co-Managing Partner<br>partners@meridian.example</p>
  </section>
</main>
</body>
</html>
```